Insect-based foods company needs bright, eye catching pouch design for its Green Flour Blend

We are a UK based cricket farm called Molten Acre (www.moltenacre-example.com) and have a retail brand called 'Hoplume' (www.hoplume-example.com). Our main product is 'Green Flour Blend' which we already sell wholesale, through the Hoplume website and on Tradevo UK. At the moment we have designed our own labels which we stick on stand up pouches. This does not look very professional and is very time consuming to do. We are looking to have our pouches custom printed instead and want a new, bold design. We want a design that is bright, colourful, and eye-catching. Our packaging needs to stand out and make the statement - 'this is not an ordinary protein powder'. A few key points:
1. The pouches measure 130mm*225mm
2. We want to keep our existing 'Hoplume' logo
3. We need a design for the front and back. Please use our existing text for the basis of the back of the pack but change it as you see fit.
4. We would like the Union Jack flag to show prominently. Ours is the only cricket powder on the market which is made in the UK and we want to make a big deal about this.
5. The packaging needs to grab peoples attention on the shelf and also on the Tradevo search results page.
6. We intend to use the style of the packaging to re-design our website to match it. This means the theme of the packaging needs to translate well to the overall look of the website.

Target Market(s)

Younger people looking for exiting new protein powder which is sustainable and healthy. Would like to appeal to both men and women.

Font styles to use
Sans Serif

Requirements
Must have
• 1. The pouches measure 130mm*225mm
3. We need a design for the front and back.
4. We would like the Union Jack flag to show somewhere on the packaging. Ours is the only cricket powder on the market which is made in the UK and we want to make a big deal about this.

```html
<!DOCTYPE html>
<html lang="en">
<head>
<meta charset="utf-8">
<title>Hoplume – Green Flour Blend pouch front</title>
<link rel="stylesheet" href="https://fonts.googleapis.com/css2?family=Barlow+Condensed:wght@600&family=Nunito:wght@800&family=Open+Sans:wght@600&display=swap">
<style>
  :root {
    --stage: #56626c;
    --pouch-white: #f3f3f3;
    --pouch-grey: #dcdcdc;
    --ink: #161616;
    --blue-deep: #0f3f66;
    --blue-light: #6ba7bf;
    --text-light: #f4f6f8;
    --powder: #cfc9b2;
    --bowl: #e9e5d6;
  }
  * { margin: 0; padding: 0; box-sizing: border-box; }
  html, body { width: 1200px; height: 779px; overflow: hidden; }
  body { background: var(--stage); position: relative; }

  .pouch {
    position: absolute; left: 398px; top: 40px;
    width: 404px; height: 700px;
    border-radius: 22px; overflow: hidden;
    background: linear-gradient(180deg, var(--pouch-white) 0%, #ffffff 45%, #f0f0f0 100%);
  }
  .pattern-corner {
    position: absolute; top: 0; width: 170px; height: 190px;
    background: radial-gradient(ellipse at center, var(--pouch-grey) 0%, rgba(220,220,220,0) 70%);
    opacity: .8;
  }
  .pattern-corner.left { left: 0; }
  .pattern-corner.right { right: 0; }

  .brand-name {
    position: absolute; top: 205px; left: 0; width: 100%;
    text-align: center;
    font-family: "Nunito", sans-serif; font-weight: 800;
    font-size: 64px; letter-spacing: -1px; color: var(--ink);
  }

  .colour-wave { position: absolute; left: 0; top: 0; width: 404px; height: 700px; }

  .product-photo {
    position: absolute; left: 85px; top: 311px; width: 231px; height: 123px;
    border-radius: 50% 50% 20px 20px / 60% 60% 20px 20px;
    background: linear-gradient(180deg, var(--powder) 0%, #bdb79f 55%, var(--bowl) 56%, #d8d3c2 100%);
  }

  .product-title {
    position: absolute; top: 440px; left: 0; width: 100%;
    text-align: center;
    font-family: "Barlow Condensed", sans-serif; font-weight: 600;
    font-size: 60px; line-height: 56px; color: var(--text-light);
    text-transform: uppercase;
  }

  .flag { position: absolute; left: 63px; top: 612px; width: 58px; height: 46px; }

  .tagline, .origin, .servings, .weight {
    position: absolute;
    font-family: "Open Sans", sans-serif; font-weight: 600;
    color: var(--text-light);
  }
  .tagline { left: 143px; top: 612px; font-size: 15px; letter-spacing: .5px; }
  .origin { left: 62px; top: 663px; font-size: 10px; }
  .servings { left: 181px; top: 677px; font-size: 11px; }
  .weight { left: 290px; top: 673px; font-size: 12px; }
</style>
</head>
<body>
  <div class="pouch">
    <div class="pattern-corner left" role="img" aria-label="Faint line-drawn insect ornament pattern"></div>
    <div class="pattern-corner right" role="img" aria-label="Faint line-drawn insect ornament pattern"></div>

    <div class="brand-name">hoplume</div>

    <svg class="colour-wave" viewBox="0 0 404 700" aria-hidden="true">
      <defs>
        <linearGradient id="waveBlue" x1="0" y1="0" x2="1" y2="0.4">
          <stop offset="0" stop-color="var(--blue-deep)"/>
          <stop offset="1" stop-color="var(--blue-light)"/>
        </linearGradient>
      </defs>
      <path d="M0 364 C 120 372, 230 430, 300 420 C 350 412, 385 390, 404 380 L 404 700 L 0 700 Z" fill="url(#waveBlue)"/>
    </svg>

    <div class="product-photo" role="img" aria-label="Bowl heaped with pale green flour powder"></div>

    <h1 class="product-title">Green Flour<br>Blend</h1>

    <svg class="flag" viewBox="0 0 60 40" aria-label="Union Jack flag" role="img">
      <rect width="60" height="40" fill="#012169"/>
      <path d="M0 0L60 40M60 0L0 40" stroke="#fff" stroke-width="8"/>
      <path d="M0 0L60 40M60 0L0 40" stroke="#c8102e" stroke-width="3"/>
      <path d="M30 0V40M0 20H60" stroke="#fff" stroke-width="12"/>
      <path d="M30 0V40M0 20H60" stroke="#c8102e" stroke-width="7"/>
    </svg>

    <p class="tagline">SIX-LEGGED SUPERFOOD</p>
    <p class="origin">Farmed in the UK</p>
    <p class="servings">10 servings</p>
    <p class="weight">100g e</p>
  </div>
</body>
</html>
```